'TOLVANTA' NEW WINE LABEL DESIGN

I am looking for an exceptional and exciting design for a wine label called 'Tolvanta' meaning 'Lookout'. The design must feature the name 'Tolvanta', and the word 'Cabernet Sauvignon' in version 1 and 'Sauvignon Blanc' in version 2. It will also need the words 'Valle Central, Chile' at the bottom of the label as a prominent piece of information as well as the vintage 2017. Please produce the work in size 80mm x 100mm. Feel free to use colour in addition to black/white and ensue that the label is easy to read on a shelf placement.
Target Market(s)
SUPERMARKETS & WINE STORES
Requirements
Must have
- EASY TO READ, USE COLOURS LIKE GREEN FOR SAUVIGNON & RED FOR CABERNET SAUVIGNON
- FULL BOTTLE SHOT MUST BE IN PROVIDED DESIGNS. ALL BOTTLE TOPS SHOULD BE QUORLAN STYLE (SCREW TOP)
- PLEASE NOTE THAT LABEL INFORMATION MUSY BE EASY TO READ I.E. VINTAGE, PLACE OF ORGIN ALTHOUGH NOT THE MAIN CONTENT MUST STILL BE CLEAR.
Nice to have
- ARTISTIC REFERENCE LINK TO NAME & ANDES BUT NOT PICTURES OF MOUNTAINS
Should not have
- PICTURES OF GRAPES
- PICTURES OF VINEYARDS
- PICTURES OF MOUNTAINS

```html
<!DOCTYPE html>
<html lang="en">
<head>
<meta charset="utf-8">
<title>Tolvanta Wine Labels</title>
<link rel="stylesheet" href="https://fonts.googleapis.com/css2?family=Oswald:wght@500;700&family=Open+Sans:wght@400;700&display=swap">
<style>
  :root {
    --page-bg: #ffffff;
    --cab-red: #a61f2c;
    --cab-band: #bf3f4b;
    --cab-line: #d9707a;
    --cab-art: #b9505a;
    --cab-ink: #ffffff;
    --blanc-green: #8c9a62;
    --blanc-green-dark: #76844f;
    --blanc-paper: #fbfaf4;
    --blanc-stripe: #f0efe6;
    --blanc-art: #4a4a44;
    --blanc-ink: #3a3a36;
  }
  * { margin: 0; padding: 0; box-sizing: border-box; }
  html, body {
    width: 825px;
    height: 1200px;
    overflow: hidden;
    background: var(--page-bg);
  }
  .label-sheet {
    width: 825px;
    height: 1200px;
    display: flex;
    justify-content: center;
    align-items: center;
    gap: 90px;
  }
  .wine-label { width: 300px; height: 350px; display: block; }
  .brand-name { font-family: "Oswald", sans-serif; font-weight: 700; letter-spacing: 1px; }
  .varietal { font-family: "Open Sans", sans-serif; }
  .region { font-family: "Open Sans", sans-serif; font-weight: 700; }
  .varietal-main { font-family: "Oswald", sans-serif; font-weight: 500; }
</style>
</head>
<body>
<main class="label-sheet">

  <!-- Version 1: Cabernet Sauvignon -->
  <svg class="wine-label label-cabernet" viewBox="0 0 300 350" aria-label="Tolvanta Cabernet Sauvignon label">
    <path d="M30 0 H270 A30 30 0 0 0 300 30 V320 A30 30 0 0 0 270 350 H30 A30 30 0 0 0 0 320 V30 A30 30 0 0 0 30 0 Z" fill="var(--cab-red)"/>
    <path d="M34 10 H266 A26 26 0 0 0 290 34 V316 A26 26 0 0 0 266 340 H34 A26 26 0 0 0 10 316 V34 A26 26 0 0 0 34 10 Z" fill="none" stroke="var(--cab-line)" stroke-width="1.5"/>
    <text class="brand-name" x="150" y="92" text-anchor="middle" font-size="42" fill="var(--cab-ink)">TOLVANTA</text>
    <rect class="varietal-band" x="10" y="112" width="280" height="40" fill="var(--cab-band)"/>
    <text class="varietal" x="150" y="139" text-anchor="middle" font-size="19" fill="var(--cab-ink)">Cabernet Sauvignon</text>
    <rect x="70" y="170" width="160" height="80" rx="10" fill="var(--cab-art)" role="img" aria-label="Line illustration of a windmill on a hilltop lookout"/>
    <path id="cab-region-arc" d="M40 255 Q150 355 260 255" fill="none"/>
    <text class="region" font-size="17" fill="var(--cab-ink)">
      <textPath href="#cab-region-arc" startOffset="50%" text-anchor="middle">Valle Central, Chile</textPath>
    </text>
  </svg>

  <!-- Version 2: Sauvignon Blanc -->
  <svg class="wine-label label-blanc" viewBox="0 0 300 350" aria-label="Tolvanta Sauvignon Blanc label">
    <path d="M30 3 H270 A27 27 0 0 0 297 30 V320 A27 27 0 0 0 270 347 H30 A27 27 0 0 0 3 320 V30 A27 27 0 0 0 30 3 Z" fill="var(--blanc-paper)" stroke="var(--blanc-green)" stroke-width="6"/>
    <path d="M36 14 H264 A22 22 0 0 0 286 36 V314 A22 22 0 0 0 264 336 H36 A22 22 0 0 0 14 314 V36 A22 22 0 0 0 36 14 Z" fill="var(--blanc-stripe)" stroke="var(--blanc-green)" stroke-width="1.5"/>
    <rect class="ribbon-band" x="14" y="98" width="272" height="30" fill="var(--blanc-green)"/>
    <ellipse class="name-oval" cx="150" cy="113" rx="90" ry="38" fill="var(--blanc-green)" stroke="var(--blanc-paper)" stroke-width="3"/>
    <text class="brand-name" x="150" y="126" text-anchor="middle" font-size="36" fill="#ffffff">TOLVANTA</text>
    <rect x="34" y="160" width="70" height="130" rx="6" fill="var(--blanc-art)" role="img" aria-label="Silhouette of a wine bottle and a filled glass"/>
    <text class="varietal-main" x="112" y="212" font-size="27" fill="var(--blanc-ink)">SAUVIGNON</text>
    <text class="varietal-main" x="110" y="262" font-size="54" fill="var(--blanc-green)">BLANC</text>
    <text class="region" x="112" y="284" font-size="14" fill="var(--blanc-green-dark)">Valle Central, Chile</text>
  </svg>

</main>
</body>
</html>
```